New layout for printer ink webiste

We require fresh ,easy to navigate layout for our online shop, everything can be changed even the logo open to ideas, We are cut price printer cartridge retailer pos is price, quality and speed of delivery. Design is for magento store website www.quillmora.ie (landing page and product page).

Target Market(s)

printer owners

Industry/Entity Type

Printer

Number of Pages Required

2 page

Requirements
Must have
• clear pricing, and what we sell.
Nice to have
• must keep quick search menu, maybe different layout
Should not have
• too much going on

```html
<!DOCTYPE html>
<html lang="en">
<head>
<meta charset="utf-8">
<title>quillmora.ie – Printer Ink &amp; Stationery</title>
<link href="https://fonts.googleapis.com/css2?family=Open+Sans:wght@400;600;700&family=Raleway:wght@500;600;700&family=Roboto:wght@400;500;700;900&display=swap" rel="stylesheet">
<style>
:root{
  --red:#e8392f;
  --red-dark:#d3261c;
  --ink:#222;
  --text:#333;
  --muted:#777;
  --line:#e3e3e3;
  --panel:#ececec;
  --button:#3b3b3b;
  --blue:#2a7fd0;
  --navy:#2b2f7a;
  --purple:#4c3f8e;
  --foot:#f2f2f2;
  --star:#f5c400;
}
*{box-sizing:border-box;margin:0;padding:0}
html,body{width:1200px;height:3141px;overflow:hidden;background:#fff}
body{position:relative;font-family:"Open Sans",Arial,sans-serif;color:var(--text)}
.abs{position:absolute}
/* top bar */
.topbar{left:0;top:0;width:1200px;height:27px;background:#111;color:#fff;font-size:11px;font-weight:600}
.topbar .care{left:52px;top:6px}
.topbar .tools{right:40px;top:0;height:27px;display:flex;align-items:center;gap:0}
.topbar .tools span{padding:0 18px;border-left:1px solid #444;line-height:27px}
/* header */
.logo{left:58px;top:52px;font-family:"Roboto",sans-serif;font-weight:900;font-size:46px;color:var(--red);letter-spacing:-1px;display:flex;align-items:center;gap:8px}
.logo i{display:block;width:14px;height:14px;background:var(--red)}
.cart{left:957px;top:52px;width:195px}
.cart .sel{height:25px;border:1px solid #ddd;font-size:11px;color:#999;padding:4px 8px;position:relative}
.cart .sel:after{content:"";position:absolute;right:10px;top:10px;border:4px solid transparent;border-top-color:#999}
.cart .sum{height:26px;border:1px solid #ddd;border-top:0;font-size:11px;color:#777;display:flex;align-items:center;justify-content:space-between;padding:0 10px}
.nav{left:80px;top:138px;display:flex;font-family:"Roboto",sans-serif;font-weight:500;font-size:14px;color:#333}
.nav a{padding:0 22px;border-left:1px solid #bbb;line-height:16px;text-decoration:none;color:inherit}
.nav a:first-child{border-left:0;position:relative}
.nav a:first-child:before{content:"";position:absolute;left:14px;right:14px;top:-11px;height:2px;background:var(--blue)}
/* hero */
.hero{left:0;top:176px;width:1200px;height:433px;background:var(--panel);overflow:hidden}
.hero .h1{left:50px;top:54px;font-family:"Roboto",sans-serif;font-weight:900;line-height:1}
.hero .pct{font-size:50px;color:var(--red)}
.hero .sat{font-size:55px;color:#444;margin-top:12px}
.hero .money{font-size:82px;color:var(--red);margin-top:6px}
.hero .money small{font-size:56px;color:#444;margin-left:4px}
.hero .art{left:60px;top:255px;width:360px;height:178px;background:linear-gradient(120deg,#2fbfa8,#1a8fcf 45%,#8cc63f 75%,#f0a32a)}
.hero .photo{left:640px;top:0;width:560px;height:395px;background:linear-gradient(160deg,#9a9a9a,#5a5a5a 40%,#d8c17a 70%,#c95a4a)}
/* promo grid */
.promo{left:46px;top:643px;width:1108px;height:438px}
.combo{left:0;top:0;width:438px;height:438px;background:#f6f6f6}
.combo .kicker{left:18px;top:57px;font-size:12px;color:#555;font-weight:600}
.combo .title{left:18px;top:76px;font-family:"Roboto",sans-serif;font-size:40px;font-weight:500;color:#444}
.combo .desc{left:18px;top:128px;width:190px;font-size:12px;line-height:19px;color:#555}
.combo .shop{left:18px;top:194px;width:106px;height:30px;border-radius:15px;background:var(--purple);color:#fff;font-size:11px;font-weight:700;text-align:center;line-height:30px}
.combo .ribbon{left:383px;top:0;width:51px;height:75px;background:#1aa0e0;color:#fff;text-align:center;font-size:13px;font-weight:700;padding-top:8px;clip-path:polygon(0 0,100% 0,100% 100%,50% 80%,0 100%)}
.combo .ribbon small{display:block;font-size:10px;font-weight:400}
.combo .pic{left:142px;top:111px;width:290px;height:252px;background:linear-gradient(135deg,#f0d000,#2aa7d8 35%,#d42a7d 60%,#222)}
.combo .band{left:0;top:364px;width:438px;height:74px;background:#e0e0e0;font-family:"Raleway",sans-serif;font-weight:600;font-size:26px;color:#444;padding:22px 38px}
.tile{width:220px;height:222px}
.tile.img{background:linear-gradient(145deg,#d7d7d7,#a9a9a9)}
.tile.color{color:#fff;text-align:center;padding:38px 18px 0}
.tile h3{font-family:"Raleway",sans-serif;font-weight:700;font-size:19px;line-height:22px}
.tile p{font-size:10px;line-height:14px;margin-top:8px}
.tile .more{font-size:11px;font-weight:700;margin-top:14px}
.tile .corner{position:absolute;right:12px;top:12px;width:28px;height:28px;border-top:2px solid #fff;border-right:2px solid #fff}
/* featured */
.rec{left:0;top:1155px;width:1200px;text-align:center;font-family:"Raleway",sans-serif;font-size:16px;color:var(--purple)}
.feat{left:0;top:1178px;width:1200px;text-align:center;font-family:"Raleway",sans-serif;font-weight:600;font-size:38px;color:#333}
.searchby{left:0;top:1250px;width:1200px;text-align:center;font-family:"Raleway",sans-serif;font-size:19px;color:#999;letter-spacing:.5px}
.finder{left:57px;top:1284px;width:1086px;height:104px;background:var(--red);display:flex;gap:22px;padding:15px 14px 0}
.finder .f{flex:1}
.finder label{display:block;color:#fff;font-size:14px;margin-bottom:8px;text-transform:uppercase}
.finder .box{height:40px;background:#fff;font-size:13px;color:#aaa;padding:10px;position:relative}
.finder .box.dd:after{content:"";position:absolute;right:14px;top:13px;width:8px;height:8px;border-right:2px solid #666;border-bottom:2px solid #666;transform:rotate(45deg)}
.card{width:250px;height:467px;border:1px solid var(--line);background:#fff;text-align:center}
.card .pic{position:absolute;left:34px;top:20px;width:180px;height:180px}
.card .sale{position:absolute;left:98px;top:-4px;background:var(--red);color:#fff;font-size:11px;font-weight:700;padding:2px 6px}
.card .price{position:absolute;left:0;right:0;top:240px;font-family:"Roboto",sans-serif;font-size:34px;color:#222}
.card .price s{font-size:14px;color:#999;margin-right:6px}
.card .name{position:absolute;left:20px;right:20px;top:290px;font-size:16px;line-height:20px;color:#444}
.card .stars{position:absolute;left:0;right:0;top:337px;color:var(--star);font-size:11px;letter-spacing:1px}
.card .btn{position:absolute;left:21px;right:21px;top:366px;height:44px;background:var(--button);color:#fff;font-family:"Roboto",sans-serif;font-weight:500;font-size:16px;line-height:44px}
.card .links{position:absolute;left:21px;right:21px;top:424px;display:flex;justify-content:space-between;font-size:12px;color:#555}
/* banner */
.banner{left:121px;top:2442px;width:939px;height:180px;border:5px solid #ddd;background:linear-gradient(90deg,#f2c200 0,#f7a800 30%,#fff 45%,#fff 70%,#f39a00 100%)}
.banner .pens{position:absolute;left:0;top:0;width:240px;height:170px;background:linear-gradient(90deg,#e84040,#f7d000,#35a0e0,#7dc242)}
.banner .cup{position:absolute;right:0;top:0;width:200px;height:170px;background:linear-gradient(160deg,#f6b100,#b24a2c 70%,#7a7a7a)}
.banner .copy{position:absolute;left:260px;top:96px;width:420px;text-align:center;font-family:"Roboto",sans-serif;font-size:25px;line-height:30px;color:#333}
.banner .copy em{font-style:normal;color:var(--red)}
/* features */
.perk{top:2666px;height:84px;background:#f3f3f3;border:1px solid #e2e2e2;display:flex;align-items:center;gap:18px;padding-left:18px;font-family:"Roboto",sans-serif;font-weight:700;font-size:21px;color:#222}
/* newsletter */
.newsbar{left:0;top:2775px;width:1200px;height:46px;background:#2a2a2a;color:#fff}
.newsbar .social{position:absolute;left:46px;top:0;width:251px;height:46px;background:var(--red);display:flex;gap:16px;align-items:center;padding-left:30px}
.newsbar .social i{display:block;width:16px;height:16px;border-radius:50%;background:#fff}
.newsbar .label{position:absolute;left:375px;top:13px;font-family:"Roboto",sans-serif;font-weight:700;font-size:17px}
.newsbar .mail{position:absolute;left:330px;top:13px}
.newsbar input{position:absolute;left:662px;top:9px;width:296px;height:28px;border:0;font-size:13px;padding:0 10px;font-family:inherit}
.newsbar .sub{position:absolute;left:972px;top:9px;width:100px;height:28px;background:var(--red);font-size:13px;text-align:center;line-height:28px}
/* footer */
.footer{left:0;top:2821px;width:1200px;height:272px;background:var(--foot)}
.col{top:37px}
.col h4{font-family:"Roboto",sans-serif;font-weight:700;font-size:18px;color:#222;margin-bottom:18px}
.col li{list-style:none;font-size:12px;line-height:28px;color:#444}
.contact li{display:flex;gap:14px;line-height:18px;margin-bottom:16px}
.contact svg{flex:none;margin-top:1px}
.badges{display:flex;gap:10px;margin-bottom:16px}
.badges b{display:block;width:40px;height:22px;border-radius:3px}
.col h5{font-family:"Roboto",sans-serif;font-weight:700;font-size:13px;color:#222;margin-bottom:14px}
.copyright{left:0;top:3093px;width:1200px;height:48px;background:#fff;font-size:12px;color:#555}
.copyright .l{position:absolute;left:58px;top:15px}
.copyright .r{position:absolute;right:60px;top:15px;display:flex;gap:32px}
</style>
</head>
<body>

<div class="abs topbar">
  <div class="abs care">CUSTOM CARE: &nbsp;888-41-2290</div>
  <div class="abs tools"><span>$ US &#9662;</span><span>&#9679; MY ACCOUNT</span><span style="padding-right:0">
    <svg width="13" height="13" viewBox="0 0 13 13" style="vertical-align:-2px"><circle cx="5.5" cy="5.5" r="4" fill="none" stroke="#fff" stroke-width="1.6"/><line x1="8.5" y1="8.5" x2="12" y2="12" stroke="#fff" stroke-width="1.8"/></svg></span></div>
</div>

<div class="abs logo"><i></i>quillmora.ie</div>

<div class="abs cart">
  <div class="sel">Your cart</div>
  <div class="sum">
    <svg width="18" height="14" viewBox="0 0 18 14"><path d="M1 2h3l2 8h9l2-6H5" fill="none" stroke="#888" stroke-width="1.5"/><circle cx="7" cy="12.5" r="1.3" fill="#888"/><circle cx="14" cy="12.5" r="1.3" fill="#888"/></svg>
    <span>0 ITEMS &nbsp;| &nbsp;$0</span>
  </div>
</div>

<nav class="abs nav">
  <a>All Products</a><a>Visiting Cards</a><a>Invitations &amp; Stationery</a><a>Printed Apparels</a><a>Marketing Materials</a><a>Embroidered Products</a>
</nav>

<section class="abs hero">
  <div class="abs photo" role="img" aria-label="Photo printer printing a spread of colourful photographs"></div>
  <div class="abs art" role="img" aria-label="Cluster of multicoloured geometric triangles"></div>
  <div class="abs h1">
    <div class="pct">100%</div>
    <div class="sat">SATISFACTION OR</div>
    <div class="money">MONEY<small>BACK</small></div>
  </div>
</section>

<section class="abs promo">
  <div class="abs combo">
    <div class="abs kicker">BUILD YOUR OWN</div>
    <div class="abs title">COMBO</div>
    <div class="abs desc">High quality products for every occasion</div>
    <div class="abs shop">SHOP NOW</div>
    <div class="abs pic" role="img" aria-label="Set of yellow, cyan, magenta and black ink cartridges"></div>
    <div class="abs ribbon">30%<small>off</small></div>
    <div class="abs band">STATIONERY COLLECTIONS</div>
  </div>
  <div class="abs tile img" style="left:452px;top:0" role="img" aria-label="Four colour ink cartridge pack"></div>
  <div class="abs tile color" style="left:676px;top:0;background:var(--red)">
    <span class="corner"></span>
    <h3>EMBROIDERED<br>PRODUCTS</h3>
    <p>Offering irresistible fashion and fast off the run way styles</p>
    <div class="more">READ MORE</div>
  </div>
  <div class="abs tile img" style="left:888px;top:0;background:linear-gradient(145deg,#e5e5e5,#c9c9c9)" role="img" aria-label="Row of colour toner cartridges"></div>
  <div class="abs tile color" style="left:452px;top:226px;background:var(--blue)">
    <span class="corner"></span>
    <h3>EMBROIDERED<br>POLOS</h3>
    <p>Offering irresistible fashion and fast off the run way styles</p>
    <div class="more">READ MORE</div>
  </div>
  <div class="abs tile img" style="left:676px;top:226px;background:linear-gradient(145deg,#ececec,#b9b9b9)" role="img" aria-label="Large format printer"></div>
  <div class="abs tile color" style="left:888px;top:226px;background:var(--navy);padding-top:58px">
    <span class="corner"></span>
    <h3>STATIONERY</h3>
    <p style="font-size:11px">EXTRA 45% OFF ALL SALE!<br>FREE SHOPPING</p>
  </div>
</section>

<div class="abs rec">We Recommend</div>
<div class="abs feat">Featured Products</div>
<div class="abs searchby">SEARCH BY BRAND, PRINTER SERIES OR CARTRIDGE</div>

<div class="abs finder">
  <div class="f"><label>Choose your brand</label><div class="box dd">Select Compatible Brand</div></div>
  <div class="f"><label>Choose your series or cartridges</label><div class="box"></div></div>
  <div class="f"><label>Select your cartridge</label><div class="box dd">Select Cartridge</div></div>
</div>

<!-- product row 1 -->
<div class="abs card" style="left:61px;top:1439px">
  <div class="pic" role="img" aria-label="Four ink cartridges" style="background:linear-gradient(135deg,#333,#1aa0e0 50%,#e8e8e8)"></div>
  <div class="price">$95.00</div><div class="name">Non-woven Document Bag</div>
  <div class="stars">★★★★★</div><div class="btn">ADD TO CART</div>
  <div class="links"><span>COMPARE</span><span>ADD TO WISHLIST</span></div>
</div>
<div class="abs card" style="left:337px;top:1439px">
  <div class="sale">SALE!</div>
  <div class="pic" role="img" aria-label="Row of colour ink cartridges" style="background:linear-gradient(135deg,#f0d000,#d42a7d 50%,#2aa7d8)"></div>
  <div class="price"><s>$75.00</s>$70.00</div><div class="name">Aztec Spooner 10 oz Mug</div>
  <div class="stars">★★★★★</div><div class="btn">ADD TO CART</div>
  <div class="links"><span>COMPARE</span><span>ADD TO WISHLIST</span></div>
</div>
<div class="abs card" style="left:613px;top:1439px">
  <div class="pic" role="img" aria-label="Tri-colour ink cartridge" style="background:linear-gradient(135deg,#222,#e8632a 50%,#2aa7d8)"></div>
  <div class="price">$100.00</div><div class="name">Luxury Slim Stand Smart Case Leather Back...</div>
  <div class="stars">★★★★★</div><div class="btn">ADD TO CART</div>
  <div class="links"><span>COMPARE</span><span>ADD TO WISHLIST</span></div>
</div>
<div class="abs card" style="left:889px;top:1439px">
  <div class="pic" role="img" aria-label="Two boxed ink cartridges" style="background:linear-gradient(135deg,#2a2a2a,#f0f0f0 50%,#d42a7d)"></div>
  <div class="price">$120.00</div><div class="name">T-Shirt Printing</div>
  <div class="stars">★★★★★</div><div class="btn">ADD TO CART</div>
  <div class="links"><span>COMPARE</span><span>ADD TO WISHLIST</span></div>
</div>

<!-- product row 2 -->
<div class="abs card" style="left:61px;top:1937px">
  <div class="pic" role="img" aria-label="Multicolour ink cartridge set" style="background:linear-gradient(135deg,#1a1a1a,#d42a7d 45%,#f0a000)"></div>
  <div class="price">$95.00</div><div class="name">Non-woven Document Bag</div>
  <div class="stars">★★★★★</div><div class="btn">ADD TO CART</div>
  <div class="links"><span>COMPARE</span><span>ADD TO WISHLIST</span></div>
</div>
<div class="abs card" style="left:337px;top:1937px">
  <div class="sale">SALE!</div>
  <div class="pic" role="img" aria-label="Boxed ink cartridge multipack" style="background:linear-gradient(135deg,#2aa7d8,#222 50%,#d42a7d)"></div>
  <div class="price"><s>$75.00</s>$70.00</div><div class="name">Aztec Spooner 10 oz Mug</div>
  <div class="stars">★★★★★</div><div class="btn">ADD TO CART</div>
  <div class="links"><span>COMPARE</span><span>ADD TO WISHLIST</span></div>
</div>
<div class="abs card" style="left:613px;top:1937px">
  <div class="pic" role="img" aria-label="Four black ink cartridges" style="background:linear-gradient(135deg,#111,#555 50%,#e8e8e8)"></div>
  <div class="price">$100.00</div><div class="name">Luxury Slim Stand Smart Case Leather Back...</div>
  <div class="stars">★★★★★</div><div class="btn">ADD TO CART</div>
  <div class="links"><span>COMPARE</span><span>ADD TO WISHLIST</span></div>
</div>
<div class="abs card" style="left:889px;top:1937px">
  <div class="pic" role="img" aria-label="Black and colour ink cartridge pair" style="background:linear-gradient(135deg,#222,#d42a7d 55%,#2aa7d8)"></div>
  <div class="price">$120.00</div><div class="name">T-Shirt Printing</div>
  <div class="stars">★★★★★</div><div class="btn">ADD TO CART</div>
  <div class="links"><span>COMPARE</span><span>ADD TO WISHLIST</span></div>
</div>

<div class="abs banner">
  <div class="pens" role="img" aria-label="Row of coloured highlighter pens"></div>
  <div class="cup" role="img" aria-label="Pencil cup with pens and pencils"></div>
  <div class="copy">Brings you a Complete Range<br>of <em>School And Office Stationery</em></div>
</div>

<div class="abs perk" style="left:52px;width:356px">
  <svg width="42" height="42" viewBox="0 0 42 42"><circle cx="21" cy="21" r="19" fill="#222"/><circle cx="21" cy="21" r="13" fill="none" stroke="#fff" stroke-width="2"/><path d="M14 21l5 5 9-10" fill="none" stroke="#fff" stroke-width="3"/></svg>
  1 YEAR GUARANTEE
</div>
<div class="abs perk" style="left:421px;width:354px">
  <svg width="46" height="36" viewBox="0 0 46 36"><circle cx="23" cy="9" r="7" fill="#222"/><path d="M11 34c0-10 6-15 12-15s12 5 12 15z" fill="#222"/><circle cx="9" cy="13" r="5" fill="#222"/><path d="M0 32c0-7 4-11 9-11 3 0 5 1 6 3-2 2-3 5-3 8z" fill="#222"/><circle cx="37" cy="13" r="5" fill="#222"/><path d="M46 32c0-7-4-11-9-11-3 0-5 1-6 3 2 2 3 5 3 8z" fill="#222"/></svg>
  24/7 CUSTOMER SERVICE
</div>
<div class="abs perk" style="left:792px;width:356px">
  <svg width="44" height="42" viewBox="0 0 44 42"><path d="M26 4c-6 10-10 15-10 22a10 10 0 0020 0c0-7-4-12-10-22z" fill="#222"/><path d="M8 2c-4 6-6 9-6 12a6 6 0 0012 0c0-3-2-6-6-12z" fill="#222"/></svg>
  GRADE A INKS USED
</div>

<div class="abs newsbar">
  <div class="social"><i></i><i></i><i></i><i></i><i></i><i></i></div>
  <svg class="mail" width="26" height="20" viewBox="0 0 26 20"><rect x="1" y="1" width="24" height="18" rx="2" fill="#fff"/><path d="M2 3l11 8 11-8" fill="none" stroke="#2a2a2a" stroke-width="2"/></svg>
  <div class="label">SIGN UP FOR OUR NEWSLETTER</div>
  <input type="text" placeholder="Enter Your Email">
  <div class="sub">Subscribe</div>
</div>

<footer class="abs footer">
  <div class="abs col contact" style="left:65px">
    <h4>CONTACT US</h4>
    <ul>
      <li><svg width="14" height="14" viewBox="0 0 14 14"><path d="M1 7L7 1l6 6v6H1z" fill="none" stroke="#666" stroke-width="1.3"/></svg><span>quillmora.ie<br>Canal Street Athlone N37 KX52 Ireland</span></li>
      <li><svg width="14" height="14" viewBox="0 0 14 14"><rect x="3" y="1" width="8" height="12" rx="1.5" fill="none" stroke="#666" stroke-width="1.3"/></svg><span>1890 402718</span></li>
      <li><svg width="14" height="14" viewBox="0 0 14 14"><rect x="1" y="3" width="12" height="8" fill="none" stroke="#666" stroke-width="1.3"/><path d="M1 3l6 5 6-5" fill="none" stroke="#666" stroke-width="1.3"/></svg><span>care@quillmora.ie</span></li>
    </ul>
  </div>
  <div class="abs col" style="left:398px">
    <h4>OUR COMPANY</h4>
    <ul><li>About us</li><li>Contact Us</li><li>Help</li><li>FAQ</li><li>Terms and Conditions</li><li>Privacy Policy</li></ul>
  </div>
  <div class="abs col" style="left:651px">
    <h4>ORDERS</h4>
    <ul><li>Recycle</li><li>Shipping &amp; Returns</li><li>Ordering Info</li><li>Cookies</li><li>My Account</li></ul>
  </div>
  <div class="abs col" style="left:934px">
    <h4>PAYMENT METHODS</h4>
    <div class="badges"><b style="background:#2a3f95"></b><b style="background:#e8632a"></b><b style="background:#4a90c8"></b><b style="background:#6aa84f"></b></div>
    <h5>SHIPPING PARTNER</h5>
    <div class="badges"><b style="background:#5a3a1e;width:30px"></b><b style="background:#5b2b8c"></b><b style="background:#e8632a"></b><b style="background:#f2c200"></b></div>
    <div class="badges"><b style="background:#c8a000"></b><b style="background:#d3261c"></b><b style="background:#1a5fa8"></b></div>
  </div>
</footer>

<div class="abs copyright">
  <div class="l">Copyright © 2014 quillmora.ie. All rights reserved.</div>
  <div class="r"><span>Privacy &amp; Cookies</span><span>Terms &amp; Conditions</span><span>Accessibility</span><span>Store Directory</span><span>About Us</span></div>
</div>

</body>
</html>
```